Need *Plum Crafted* Events Company Website
Bright Harbor Gatherings Website
Need *Plum Crafted* Events Company Website - Events
Creative Brief
Events
www.brightharborgatherings.example
Bright Harbor Gatherings (BHG) is a multi-dimensional event management firm providing all aspects of support and expertise for any special event. By providing upscale and individualized service, our events are unique and tailored around your personal vision, style and budget.
We provide partial and full-service event coordination services for all types of events; specializing in corporate meetings, conferences, receptions, and everyday social events.
We like unique and captivating web design that illustrates the characteristics of our brand and service offerrings. Our logo speaks to a company that is unique and classy with an edge. DISLIKE: Black or extremely dark backgrounds. Too fancy flash applications, Music or any kind of intro, anything that is too elaborate. LIKE: Easy flow and simplicity. I like the mix of soft neutrals
Feminine
neutral tones
pop of red
complementary tones
right side
www.vowlantern.example
www.quillaffairs.example
Will attached websites that we like later Please use the Fonts from my logo: Will attach files I would like for you to use the accent color on my logo as an special accent only so my logo is not overpowered. I am open to navigation placement but it does not give me that option so I selected what I believe is my personal preference.

```html
<!DOCTYPE html>
<html lang="en">
<head>
<meta charset="utf-8">
<title>Bright Harbor Gatherings</title>
<link href="https://fonts.googleapis.com/css2?family=Crimson+Text:ital,wght@0,400;0,600;1,400;1,600&family=Cinzel:wght@400;600&display=swap" rel="stylesheet">
<style>
:root{
  --brown:#5a3e36;
  --brown-dark:#46302a;
  --cream:#ece7cf;
  --cream-light:#f5f2e2;
  --cream-deep:#dcd6b7;
  --stripe:#e3ddc2;
  --frame:#f7f5ea;
  --line:#b9b195;
  --red:#b8343a;
  --red-soft:#c9454a;
  --text:#6b5a50;
  --muted:#8a7c70;
  --teal:#7d8f86;
}
*{margin:0;padding:0;box-sizing:border-box}
html,body{width:1200px;height:823px;overflow:hidden}
body{position:relative;background:var(--cream);font-family:"Crimson Text",Georgia,serif;color:var(--text)}
.side{position:absolute;top:0;bottom:0;width:48px;background:var(--brown)}
.side--left{left:0}.side--right{right:0}
.backdrop{position:absolute;left:48px;right:48px;top:0;height:700px;background:radial-gradient(ellipse at 50% 40%,var(--cream-light),var(--cream) 70%,var(--cream-deep))}
.stripes{position:absolute;left:48px;right:48px;top:700px;bottom:0;background:repeating-linear-gradient(90deg,var(--stripe) 0 18px,var(--cream) 18px 36px)}
.nav{position:absolute;left:408px;top:46px;width:630px;height:40px;background:var(--frame);border:1px solid var(--line);display:flex;align-items:center;padding:0 10px;gap:0}
.nav a{font-family:"Cinzel",Georgia,serif;font-size:14px;color:var(--text);text-decoration:none;padding:0 11px;border-right:1px solid var(--line);line-height:16px}
.nav a.is-active{color:var(--red)}
.nav a:nth-last-child(2){border-right:none}
.nav .nav__pdf{margin-left:auto;border:1px solid var(--line);padding:3px 10px;font-size:10px;letter-spacing:1px;background:var(--cream-light)}
.hero{position:absolute;left:113px;top:96px;width:943px;height:288px;background:var(--frame);border:1px solid var(--line);box-shadow:0 2px 6px rgba(0,0,0,.15)}
.hero__brand{position:absolute;left:12px;top:12px;width:211px;height:262px;background:var(--cream-light);border:2px solid var(--brown);display:flex;align-items:center;justify-content:center;text-align:center}
.hero__brand span{font-family:"Crimson Text",Georgia,serif;font-weight:600;font-size:24px;line-height:1.2;color:var(--brown);padding:0 20px}
.hero__photo{position:absolute;left:228px;top:10px;width:708px;height:259px;background:linear-gradient(135deg,#f4efe8,#e6d8c8 45%,#cfc2b0 70%,#eef0ec)}
.hero__cta{position:absolute;right:8px;bottom:34px;width:230px;height:58px;background:var(--teal);transform:skewY(-10deg);color:#fff;text-align:center;padding-top:6px}
.hero__cta b{display:block;font-family:"Cinzel",Georgia,serif;font-weight:400;font-size:20px;letter-spacing:1px}
.hero__cta i{display:inline-block;font-style:normal;font-size:11px;letter-spacing:1px;background:var(--brown);padding:1px 10px;font-family:"Cinzel",Georgia,serif}
.hero__dots{position:absolute;right:14px;bottom:4px;display:flex;gap:5px}
.hero__dots span{width:7px;height:7px;border-radius:50%;background:var(--brown)}
.tabs{position:absolute;left:1057px;top:118px;display:flex;flex-direction:column;gap:8px}
.tabs a{width:22px;height:56px;background:var(--red-soft);color:#fff;font-size:9px;font-family:"Cinzel",Georgia,serif;text-decoration:none;writing-mode:vertical-rl;display:flex;align-items:center;justify-content:center;border-radius:0 4px 4px 0}
.card{position:absolute;top:408px;width:302px;height:235px;background:var(--frame);border:1px solid var(--line);padding:9px;box-shadow:0 2px 5px rgba(0,0,0,.15)}
.card__photo{height:160px}
.card--gallery{left:120px}
.card--gallery .card__photo{background:linear-gradient(180deg,#c9c6bf,#8b8f9a 55%,#3f3f70)}
.card--services{left:451px}
.card--services .card__photo{background:linear-gradient(135deg,#e9e6de,#f7f5ef 50%,#9a9f8a)}
.card h2{font-style:italic;font-weight:600;color:var(--red);font-size:21px;margin-top:6px;line-height:1.1}
.card p{font-style:italic;font-size:14px;color:var(--text)}
.video{position:absolute;left:773px;top:408px;width:297px;height:235px;background:var(--frame);border:1px solid var(--line);padding:9px;box-shadow:0 2px 5px rgba(0,0,0,.15)}
.video__screen{position:relative;height:100%;background:radial-gradient(circle,#6e4d47,var(--brown-dark));display:flex;align-items:center;justify-content:center}
.video__mark{position:absolute;top:30px;left:50%;transform:translateX(-50%);width:70px;height:130px;background:rgba(180,150,140,.25)}
.video__screen svg{position:relative}
.footer{position:absolute;left:120px;top:732px;width:955px;height:40px;background:var(--frame);border:1px solid var(--line);display:flex;align-items:center;justify-content:space-between;padding:0 16px;font-style:italic;font-size:10px;color:var(--muted)}
</style>
</head>
<body>
<div class="side side--left"></div>
<div class="side side--right"></div>
<div class="backdrop" role="img" aria-label="Soft cream damask wall pattern"></div>
<div class="stripes"></div>

<nav class="nav">
  <a href="#" class="is-active">Home</a>
  <a href="#">About Us</a>
  <a href="#">Services</a>
  <a href="#">Contact Us</a>
  <a href="#">Events</a>
  <a href="#">Our Blog</a>
  <a href="#" class="nav__pdf">DOWNLOAD PDF</a>
</nav>

<section class="hero">
  <div class="hero__brand"><span>Bright Harbor Gatherings</span></div>
  <div class="hero__photo" role="img" aria-label="Elegant reception table with glassware, plates and pink flowers"></div>
  <a class="hero__cta" href="#"><b>WHY CHOOSE US</b><i>CLICK HERE</i></a>
  <div class="hero__dots"><span></span><span></span><span></span></div>
</section>

<div class="tabs">
  <a href="#">Share</a>
  <a href="#">Follow</a>
  <a href="#">Connect</a>
</div>

<article class="card card--gallery">
  <div class="card__photo" role="img" aria-label="Conference hall set with rows of chairs"></div>
  <h2>Photo Gallery</h2>
  <p>View portfolion and hear testimonials...</p>
</article>

<article class="card card--services">
  <div class="card__photo" role="img" aria-label="Tiered white wedding cake with flowers on a reception table"></div>
  <h2>Services</h2>
  <p>Seminars, Parties, Receptions, and more...</p>
</article>

<div class="video">
  <div class="video__screen" role="img" aria-label="Video player with faint brand mark">
    <div class="video__mark"></div>
    <svg width="44" height="44" viewBox="0 0 44 44"><circle cx="22" cy="22" r="20" fill="rgba(0,0,0,.45)"/><path d="M17 13 L32 22 L17 31 Z" fill="#f5f2e2"/></svg>
  </div>
</div>

<footer class="footer">
  <span>Copyright 2011 © Bright Harbor Gatherings. All Rights Reserved.</span>
  <span>phone 123.456.7890 &nbsp;|&nbsp; email: info@brightharborgatherings.example</span>
  <span>photography by Photographer's Name Goes Here</span>
</footer>
</body>
</html>
```